Bref créative
Martin L. Hollis
Attorney & Counselor at Law
I need double sided standard sized Business Card [3.5" x 2"]
Use different font, but that coordinates with the logo font. I am open to different variations.
Simple
20847 52nd Ave Ct SW, Ste 214
Lakewood, WA 98512
martin@martinlhollis.com
http://www.martinlhollis.com
The logo that should be used on the card should be the second version that I had the artist prepare.
Add my email address on the front of the card.
Email Address: martin@martinlhollis.com
[Insert business logo at top]
[Smaller font] Established 1982
[Larger font with bullet each line]
Divorce & Family Law
Domestic Violence
DUI & Other Criminal Defense
Bankruptcy
I have been requested to upload the *.ai file. Here it is.
This is the *.ai file for the alternate design. This is a variation on the first design. I would like to see what each one looks like on the business card. This design will save space on the card because the logo is on the same line as the text.

```html
<!DOCTYPE html>
<html lang="en">
<head>
<meta charset="utf-8">
<title>Martin L. Hollis — Business Card</title>
<link rel="stylesheet" href="https://fonts.googleapis.com/css2?family=Cinzel:wght@400;600;700&display=swap">
<style>
  :root {
    --backdrop: #e9e7e4;
    --card: #ffffff;
    --brown: #6b4220;
    --brown-dark: #3f2410;
    --brown-light: #9a6a3c;
    --blue: #1f7fb0;
    --ink: #3a3a3a;
    --icon: #3b3b3b;
  }
  html, body {
    margin: 0;
    width: 1200px;
    height: 902px;
    overflow: hidden;
    background: var(--backdrop);
  }
  .card {
    position: absolute;
    left: 100px;
    top: 165px;
    width: 1000px;
    height: 572px;
    background: var(--card);
    box-shadow: 0 10px 30px rgba(0,0,0,0.18);
    font-family: "Cinzel", serif;
    color: var(--ink);
    overflow: hidden;
  }
  .brand {
    position: absolute;
    left: 40px;
    top: 100px;
    width: 500px;
    text-align: center;
  }
  .brand-mark {
    display: block;
    width: 48px;
    height: 48px;
    margin: 0 auto 14px;
    border-radius: 50%;
    background: var(--brown);
  }
  .brand-name {
    font-family: "Cinzel", serif;
    font-weight: 700;
    font-size: 40px;
    line-height: 1;
    letter-spacing: 0.5px;
    white-space: nowrap;
    color: var(--brown);
  }
  .brand-tagline {
    margin-top: 8px;
    font-weight: 600;
    font-size: 19px;
    letter-spacing: 0.5px;
    white-space: nowrap;
    color: var(--blue);
  }
  .holder {
    position: absolute;
    left: 0;
    top: 318px;
    display: flex;
    align-items: center;
  }
  .holder-marker {
    width: 0;
    height: 0;
    border-top: 11px solid transparent;
    border-bottom: 11px solid transparent;
    border-left: 16px solid var(--blue);
  }
  .holder-name {
    margin-left: 72px;
    font-size: 18px;
    white-space: nowrap;
    color: var(--ink);
  }
  .contacts {
    position: absolute;
    left: 590px;
    top: 330px;
    margin: 0;
    padding: 0;
    list-style: none;
    font-size: 16px;
    line-height: 1;
  }
  .contacts li {
    display: flex;
    align-items: center;
    height: 27px;
    white-space: nowrap;
  }
  .contacts li.address-line {
    padding-left: 29px;
  }
  .contacts svg {
    width: 19px;
    height: 19px;
    margin-right: 10px;
    flex: none;
  }
  .side-band {
    position: absolute;
    right: 0;
    top: 0;
    width: 58px;
    height: 100%;
    background: linear-gradient(90deg, var(--brown-light), var(--brown) 45%, var(--brown-dark));
    display: flex;
    align-items: center;
    justify-content: center;
  }
  .side-band-url {
    transform: rotate(90deg);
    white-space: nowrap;
    color: #f4e7d6;
    font-size: 17px;
    letter-spacing: 2px;
  }
</style>
</head>
<body>
  <div class="card">
    <div class="brand">
      <span class="brand-mark"></span>
      <div class="brand-name">Martin L. Hollis</div>
      <div class="brand-tagline">Attorney &amp; Counselor at Law</div>
    </div>

    <div class="holder">
      <span class="holder-marker"></span>
      <span class="holder-name">Martin L. Hollis</span>
    </div>

    <ul class="contacts">
      <li>
        <svg viewBox="0 0 20 20"><circle cx="10" cy="10" r="10" fill="var(--icon)"/><path d="M10 4.5l5 4.5h-1.5v6h-7v-6H5z" fill="#fff"/></svg>
        20847 52nd Ave Ct SW, Ste 214
      </li>
      <li class="address-line">Lakewood, WA 98512</li>
      <li>
        <svg viewBox="0 0 20 20"><circle cx="10" cy="10" r="10" fill="var(--icon)"/><path d="M7 5h2l1 3-1.5 1a7 7 0 0 0 3 3l1-1.5 3 1v2c0 1-1 1.5-2 1.5A9 9 0 0 1 5.5 7c0-1 .5-2 1.5-2z" fill="#fff"/></svg>
        (253) 555-0142
      </li>
      <li>
        <svg viewBox="0 0 20 20"><circle cx="10" cy="10" r="10" fill="var(--icon)"/><rect x="6" y="5" width="8" height="4" fill="#fff"/><rect x="5" y="9" width="10" height="5" rx="1" fill="#fff"/></svg>
        (253) 555-0178
      </li>
      <li>
        <svg viewBox="0 0 20 20"><circle cx="10" cy="10" r="10" fill="var(--icon)"/><rect x="5" y="6.5" width="10" height="7" fill="#fff"/><path d="M5 6.5l5 4 5-4" fill="none" stroke="var(--icon)" stroke-width="1"/></svg>
        martin@martinlhollis.com
      </li>
      <li>
        <svg viewBox="0 0 20 20"><circle cx="10" cy="10" r="10" fill="var(--icon)"/><circle cx="10" cy="10" r="5" fill="none" stroke="#fff" stroke-width="1.2"/><path d="M5 10h10M10 5c-2.5 3-2.5 7 0 10M10 5c2.5 3 2.5 7 0 10" fill="none" stroke="#fff" stroke-width="1"/></svg>
        www.martinlhollis.com
      </li>
    </ul>

    <div class="side-band">
      <span class="side-band-url">www.MartinLHollis.com</span>
    </div>
  </div>
</body>
</html>
```